Bramblewick Co Leaflet. A5 2-sided Flyer for a UK Lawn Treatment Company

I need an A5 two-side leaflet / flyer designed for my Lawn Treatment company. The leaflet will be for door-drops so quick impact needed. Full colour, both sides. I provide lawn treatments to customers in the Exeter area of Devon. I would like to design to be clear, fresh and reflect the joy a good lawn and garden can bring.

Target Market(s)

Home Owners. 30-80 Years. Familys

Font styles to use
Sans Serif

Colors
9bcb3c
f78f20
ec1f27
33a6d7

Requirements
Must have
• Good front page picture
• Logo
• Contact details on front.
• Call to Action
• More details in Text file included in design.
Nice to have
• Clipart of a family / lady enjoying a lawn.

```html
<!DOCTYPE html>
<html lang="en">
<head>
<meta charset="utf-8">
<title>Bramblewick Co Leaflet</title>
<link href="https://fonts.googleapis.com/css2?family=Open+Sans:wght@400;600;700;800&display=swap" rel="stylesheet">
<style>
:root{
  --green:#9bcb3c;
  --green-dark:#2f8a2f;
  --green-deep:#1f6b25;
  --orange:#f78f20;
  --red:#ec1f27;
  --blue:#33a6d7;
  --ink:#3a3a3a;
  --paper:#ffffff;
  --backdrop:#e6e7e8;
}
*{margin:0;padding:0;box-sizing:border-box}
html,body{width:807px;height:1200px;overflow:hidden;background:var(--backdrop);font-family:"Open Sans",Arial,sans-serif;color:var(--ink)}
.canvas{position:relative;width:807px;height:1200px}
.page{position:absolute;width:390px;height:552px;background:var(--paper);overflow:hidden;box-shadow:0 6px 18px rgba(0,0,0,.18)}
.page--front{left:24px;top:30px}
.page--back{left:393px;top:618px}
.abs{position:absolute}
.brand{display:flex;align-items:center;gap:6px;color:var(--green-dark);font-weight:800;font-size:15px}
.brand__dot{width:12px;height:12px;border-radius:50%;background:var(--green)}
/* front */
.hero-photo{left:0;top:0;width:228px;height:240px;background:linear-gradient(160deg,#d9e9c4 0%,#8fbf55 55%,#4f8f2a 100%)}
.front .brand{left:240px;top:40px}
.tagline-small{left:244px;top:64px;font-size:8px;color:var(--green-deep);font-weight:600}
.swoosh{left:0;top:200px;width:390px;height:80px}
.headline{left:20px;top:268px;width:220px;font-size:23px;line-height:1.12;font-weight:700;color:var(--red)}
.lawn-circle{border-radius:50%;border:3px solid #fff;box-shadow:0 1px 4px rgba(0,0,0,.25)}
.lc1{left:250px;top:262px;width:110px;height:110px;background:radial-gradient(circle at 40% 40%,#b6dc78,#4e8f2b)}
.lc2{left:228px;top:366px;width:80px;height:80px;background:radial-gradient(circle at 50% 40%,#c7e39a,#5c9a33)}
.lc3{left:300px;top:372px;width:78px;height:78px;background:radial-gradient(circle at 50% 50%,#a7d267,#3f7f24)}
.front-foot{left:0;top:445px;width:390px;height:107px;background:linear-gradient(180deg,var(--green) 0%,var(--green-dark) 100%)}
.contact{left:18px;top:462px;color:#fff;font-size:9px;line-height:1.45}
.contact strong{font-size:10px;font-weight:800;display:block}
.contact .phone{display:flex;align-items:center;gap:5px;font-weight:700;font-size:11px}
.social{left:236px;top:508px;color:#fff;font-size:8.5px;font-weight:600}
/* back */
.back .brand{left:22px;top:22px}
.back-swoosh{left:0;top:50px;width:390px;height:60px}
.droplet{left:262px;top:14px;width:118px;height:90px;border-radius:10px;background:radial-gradient(circle at 45% 45%,#e8f6fb 0%,#8fd0e8 25%,#5aa63a 60%,#2f7a22 100%)}
.copy{left:22px;top:120px;width:346px}
.copy h3{font-size:10.5px;font-weight:800;color:var(--green-dark);margin-top:8px}
.copy h3.alt{color:var(--orange)}
.copy p{font-size:8px;line-height:1.4;margin-top:2px}
.services{left:22px;top:330px;width:346px;display:grid;grid-template-columns:repeat(3,1fr);gap:6px 8px;list-style:none;font-size:8px;font-weight:600;color:var(--green-deep)}
.services li{display:flex;align-items:center;gap:4px}
.back-foot{left:0;top:410px;width:390px;height:142px;background:linear-gradient(180deg,#7fb13a 0%,var(--green-dark) 55%,var(--green-deep) 100%)}
.back-foot__wave{left:0;top:396px;width:390px;height:30px}
.back-foot__text{left:22px;top:448px;width:346px;color:#fff;font-size:8.5px;line-height:1.4;text-align:center}
.cta{left:0;top:490px;width:390px;text-align:center;color:#fff;font-size:22px;font-weight:800}
</style>
</head>
<body>
<div class="canvas">

  <section class="page page--front front">
    <div class="abs hero-photo" role="img" aria-label="Photo of children relaxing together on a green lawn"></div>
    <div class="abs brand"><span class="brand__dot"></span>Bramblewick Co</div>
    <div class="abs tagline-small">Lawn treatments &amp; care</div>
    <svg class="abs swoosh" viewBox="0 0 390 80" aria-hidden="true">
      <path d="M0 40 C120 10 260 70 390 20 L390 80 L0 80 Z" fill="var(--paper)"/>
      <path d="M0 38 C120 8 260 68 390 18" stroke="var(--orange)" stroke-width="4" fill="none"/>
      <path d="M0 46 C120 16 260 76 390 26" stroke="var(--green)" stroke-width="5" fill="none"/>
    </svg>
    <h1 class="abs headline">Treatments and advice to keep your lawn looking nice.</h1>
    <div class="abs lawn-circle lc1" role="img" aria-label="Photo of a neat striped garden lawn"></div>
    <div class="abs lawn-circle lc2" role="img" aria-label="Photo of a garden with trees and grass"></div>
    <div class="abs lawn-circle lc3" role="img" aria-label="Photo of a close-up of healthy grass"></div>
    <div class="abs front-foot"></div>
    <div class="abs contact">
      <strong>Call today to book your<br>FREE LAWN SURVEY</strong>
      <span class="phone"><svg width="10" height="10" viewBox="0 0 24 24"><path fill="#fff" d="M6.6 10.8a15 15 0 006.6 6.6l2.2-2.2c.3-.3.7-.4 1-.2 1.1.4 2.3.6 3.6.6.6 0 1 .4 1 1V20c0 .6-.4 1-1 1A17 17 0 013 4c0-.6.4-1 1-1h3.5c.6 0 1 .4 1 1 0 1.3.2 2.5.6 3.6.1.3 0 .7-.2 1z"/></svg>01392 570418</span>
      <span class="phone"><svg width="10" height="10" viewBox="0 0 24 24"><rect x="7" y="2" width="10" height="20" rx="2" fill="#fff"/></svg>07700 900417</span>
      www.bramblewickco.co.uk
    </div>
    <div class="abs social">Join us on social media</div>
  </section>

  <section class="page page--back back">
    <div class="abs brand"><span class="brand__dot"></span>Bramblewick Co</div>
    <div class="abs droplet" role="img" aria-label="Photo of a water droplet on a blade of grass"></div>
    <svg class="abs back-swoosh" viewBox="0 0 390 60" aria-hidden="true">
      <path d="M0 30 C130 5 250 55 390 20" stroke="var(--orange)" stroke-width="4" fill="none"/>
      <path d="M0 38 C130 13 250 63 390 28" stroke="var(--green)" stroke-width="5" fill="none"/>
    </svg>
    <div class="abs copy">
      <h3>For a beautiful trouble-free lawn</h3>
      <p>Healthy green lawns need regular care through every season of the year.</p>
      <h3 class="alt">I will understand your lawn</h3>
      <p>I visit your garden, test the soil and plan treatments that suit it.</p>
      <h3>Your lawn treatment</h3>
      <p>Each visit is tailored to your grass, soil and the time of year.</p>
      <h3 class="alt">Industry leading lawn care</h3>
      <p>Trained, insured and friendly, using proven products that are safe for families and pets.</p>
    </div>
    <ul class="abs services">
      <li><svg width="9" height="9" viewBox="0 0 10 10"><path d="M1 5l3 3 5-7" stroke="var(--green)" stroke-width="2" fill="none"/></svg>Scarification</li>
      <li><svg width="9" height="9" viewBox="0 0 10 10"><path d="M1 5l3 3 5-7" stroke="var(--green)" stroke-width="2" fill="none"/></svg>Aeration</li>
      <li><svg width="9" height="9" viewBox="0 0 10 10"><path d="M1 5l3 3 5-7" stroke="var(--green)" stroke-width="2" fill="none"/></svg>Moss Control</li>
      <li><svg width="9" height="9" viewBox="0 0 10 10"><path d="M1 5l3 3 5-7" stroke="var(--green)" stroke-width="2" fill="none"/></svg>Overseeding</li>
      <li><svg width="9" height="9" viewBox="0 0 10 10"><path d="M1 5l3 3 5-7" stroke="var(--green)" stroke-width="2" fill="none"/></svg>Top Dressing</li>
      <li><svg width="9" height="9" viewBox="0 0 10 10"><path d="M1 5l3 3 5-7" stroke="var(--green)" stroke-width="2" fill="none"/></svg>Lawn Repairs</li>
      <li><svg width="9" height="9" viewBox="0 0 10 10"><path d="M1 5l3 3 5-7" stroke="var(--green)" stroke-width="2" fill="none"/></svg>Fertiliser &amp; Weed</li>
      <li><svg width="9" height="9" viewBox="0 0 10 10"><path d="M1 5l3 3 5-7" stroke="var(--green)" stroke-width="2" fill="none"/></svg>Pest &amp; Disease</li>
      <li><svg width="9" height="9" viewBox="0 0 10 10"><path d="M1 5l3 3 5-7" stroke="var(--green)" stroke-width="2" fill="none"/></svg>Special Events</li>
    </ul>
    <div class="abs back-foot" role="img" aria-label="Photo of a lush green grass lawn"></div>
    <svg class="abs back-foot__wave" viewBox="0 0 390 30" aria-hidden="true">
      <path d="M0 0 L390 0 L390 8 C260 30 130 0 0 22 Z" fill="var(--paper)"/>
      <path d="M0 22 C130 0 260 30 390 8" stroke="var(--orange)" stroke-width="3" fill="none"/>
    </svg>
    <p class="abs back-foot__text">Save time and money with regular visits and enjoy a lawn you are proud of.</p>
    <div class="abs cta">Call 01392 570418 Today.</div>
  </section>

</div>
</body>
</html>
```